card design for engineering consultancy

engineering drafting and project management company the provides drafting services for.
Electrical, Hydraulic, Mechanical, and Civil services
The company is called Q7R Services and logo is as attached
Information on card should be.
1. Logo
2.website : Q7RServices.example
3. email : info@Q7RServices.example
4. Phone: (+61) 400512836
5. Motto: Design - Document - Develop - Deliver

this card should be basically used for business identification only

Target Market(s)

electricians plumbers air conditioning installers and civil contractors

Industry/Entity Type

engineering, drafting, electrical, plumbing, airconditioning, civil

Contact Information for Business Card

1. Logo 2.website : Q7RServices.example 3. email : info@Q7RServices.example 4. Phone: (+61) 400512836 5. Motto: Design - Document - Develop - Deliver

Font styles to use
Serif

Requirements
Must have
• logo
Nice to have
• something inovative and different that makes it stand out from being just another business card

```html
<!DOCTYPE html>
<html lang="en">
<head>
<meta charset="utf-8">
<title>Q7R Services – Business Card</title>
<link rel="stylesheet" href="https://fonts.googleapis.com/css2?family=Montserrat:wght@400;500;700&family=Oswald:wght@500&display=swap">
<style>
  :root {
    --stage: #2b2b2d;
    --card-dark: #2e2f31;
    --card-light: #ffffff;
    --brand-grey: #4a4a4c;
    --brand-grey-soft: #6b6c70;
    --brand-red: #d0202a;
    --text-dark: #3a3a3c;
  }
  * { box-sizing: border-box; margin: 0; padding: 0; }
  html, body { width: 1200px; height: 1186px; overflow: hidden; }
  body {
    background: var(--stage);
    font-family: "Montserrat", Arial, sans-serif;
    position: relative;
  }
  .card {
    position: absolute;
    left: 220px;
    width: 760px;
    height: 434px;
    border-radius: 26px;
    overflow: hidden;
  }
  /* Back side */
  .card--back {
    top: 110px;
    background: var(--card-dark);
    border-bottom: 10px solid var(--brand-red);
    display: flex;
    align-items: center;
    justify-content: center;
  }
  .card--back .wordmark { color: var(--brand-grey-soft); font-size: 62px; }
  /* Front side */
  .card--front {
    top: 640px;
    background: var(--card-light);
  }
  .wordmark {
    display: flex;
    align-items: center;
    gap: 18px;
    font-weight: 700;
    letter-spacing: 3px;
    text-transform: uppercase;
    white-space: nowrap;
  }
  .wordmark__mark {
    width: 0.62em;
    height: 0.62em;
    background: var(--brand-red);
  }
  .card--front .wordmark {
    position: absolute;
    top: 70px;
    left: 0; right: 0;
    justify-content: center;
    color: var(--brand-grey);
    font-size: 54px;
  }
  .identity {
    position: absolute;
    top: 196px;
    left: 0; right: 0;
    display: flex;
    justify-content: center;
    align-items: center;
  }
  .person { text-align: right; padding-right: 26px; }
  .person__name { color: var(--brand-red); font-weight: 700; font-size: 27px; }
  .person__role { color: var(--text-dark); font-size: 17px; margin-top: 2px; }
  .divider { width: 2px; height: 96px; background: var(--brand-red); }
  .contacts { list-style: none; padding-left: 26px; }
  .contacts li {
    display: flex; align-items: center; gap: 12px;
    color: var(--text-dark); font-size: 18px; line-height: 31px;
  }
  .contacts svg { width: 15px; height: 15px; fill: var(--brand-red); flex: none; }
  .motto-band {
    position: absolute;
    left: 0; right: 0;
    bottom: 46px;
    height: 66px;
    background: var(--brand-red);
    display: flex;
    justify-content: center;
    align-items: center;
    gap: 30px;
    font-family: "Oswald", "Arial Narrow", sans-serif;
    font-weight: 500;
    font-size: 26px;
    letter-spacing: 1px;
    color: #fff;
    text-transform: uppercase;
  }
  .motto-band span::before { content: "•"; margin-right: 10px; }
</style>
</head>
<body>
  <section class="card card--back" aria-label="Card back">
    <div class="wordmark"><span class="wordmark__mark"></span>Q7R Services</div>
  </section>

  <section class="card card--front" aria-label="Card front">
    <div class="wordmark"><span class="wordmark__mark"></span>Q7R Services</div>

    <div class="identity">
      <div class="person">
        <p class="person__name">Daniel Hart</p>
        <p class="person__role">CEO &amp; Founder</p>
      </div>
      <div class="divider"></div>
      <ul class="contacts">
        <li>
          <svg viewBox="0 0 16 16" aria-hidden="true"><path d="M3.5 1.5l2.5 0 1.2 3.2-1.6 1.2c.8 1.7 2.1 3 3.8 3.8l1.2-1.6 3.2 1.2 0 2.5c0 .8-.7 1.5-1.5 1.5C6.8 13.3 2.7 9.2 2 3c0-.8.7-1.5 1.5-1.5z"/></svg>
          (+61) 400512836
        </li>
        <li>
          <svg viewBox="0 0 16 16" aria-hidden="true"><path d="M1 3h14v10H1z M1.8 3.6L8 8.6l6.2-5" stroke="#fff" stroke-width="1.2"/></svg>
          info@Q7RServices.example
        </li>
        <li>
          <svg viewBox="0 0 16 16" aria-hidden="true"><circle cx="8" cy="8" r="7"/><path d="M1 8h14M8 1c-2.5 3-2.5 11 0 14M8 1c2.5 3 2.5 11 0 14" stroke="#fff" stroke-width="1" fill="none"/></svg>
          Q7RServices.example
        </li>
      </ul>
    </div>

    <div class="motto-band">
      <span>Design</span><span>Document</span><span>Develop</span><span>Deliver</span>
    </div>
  </section>
</body>
</html>
```